Navory - макеты для постов в VK и TG
Задание на дизайн
Какой товар или услуга будет рекламироваться?
сервис по продаже недвижимости (квартиры)
макеты для TG vk
использованы будут для публикации в группе / канале сервиса, а так же для рекламного продвижения согласно контент плану
темы контент плана:
Пост 1. «Комиссия риелтора — это как скрытый налог»
Пост 2. «Риелтор ≠ маг и волшебник»
Пост 3. «Кто работает — вы или риелтор?»
Пост 4. «Риелтору выгодно, чтобы вы продали дешевле»
Пост 5. «Юридические риски: риелтор не всегда спасает»
Пост 6. «Риелтор как такси за миллион»
желательно что бы макеты содержали элементы фирменного стиля (шрифт, цвет ..)
https://files.pelmaroshare.net/folders/7kq48TzrbnLeoXvamPsUdcQwyhiFJRt_?usp=share_link
задача: пользователь должен заинтересоваться макетом и пойти читать полный объем текста, желательно еще и подписался
На каких сайтах будет размещаться баннер
vk, tg
Размер баннера
600 px × 600 px
Тип баннера
Статический

```html
<!DOCTYPE html>
<html lang="ru">
<head>
<meta charset="utf-8">
<title>Navory — посты для VK и TG</title>
<link rel="stylesheet" href="https://fonts.googleapis.com/css2?family=Montserrat:wght@400;500&display=swap">
<style>
:root{
  --stage:#3b3b3b;
  --green:#5e9f7f;
  --green-deep:#3f7a5e;
  --mint:#dcece3;
  --mint-soft:#eaf3ee;
  --paper:#f6f7f6;
  --ink:#1f2a24;
  --white:#ffffff;
}
*{margin:0;padding:0;box-sizing:border-box}
html,body{width:1200px;height:915px;overflow:hidden;background:var(--stage)}
body{font-family:"Montserrat",sans-serif;position:relative}
.post{position:absolute;width:408px;height:406px;overflow:hidden}
.row-1{top:34px}.row-2{top:475px}
.col-1{left:-45px}.col-2{left:396px}.col-3{left:838px}
.photo{position:absolute}
.brand{position:absolute;font-size:14px;font-weight:500;letter-spacing:.5px;display:flex;flex-direction:column;line-height:1}
.brand small{font-size:4px;font-weight:400;letter-spacing:.2px;margin-top:2px;opacity:.8}
.site{position:absolute;font-size:11px;font-weight:400}
.headline{position:absolute;font-weight:400;line-height:1.2}
svg.deco{position:absolute;inset:0}

/* post 1 */
.p1{background:var(--green)}
.p1 .photo{inset:0;background:linear-gradient(180deg,#8fbfa5 0%,#5e9f7f 45%,#4c8a6b 75%,#5a9a7a 100%);opacity:.95}
.p1 .headline{left:18px;top:250px;color:var(--white);font-size:24px}
.p1 .site{left:18px;bottom:18px;color:var(--white)}

/* post 2 */
.p2{background:var(--mint)}
.p2 .photo{left:0;top:0;width:408px;height:271px;background:linear-gradient(135deg,#c8cbc6 0%,#9a9a92 45%,#6e6a62 100%)}
.p2 .brand{right:20px;top:16px;color:var(--white)}
.p2 .headline{left:24px;top:316px;color:var(--ink);font-size:22px;text-transform:uppercase}
.p2 .site{right:20px;bottom:18px;color:var(--ink)}

/* post 3 */
.p3{background:var(--paper)}
.p3 .brand{left:20px;top:16px;color:var(--ink)}
.p3 .site{right:-10px;top:18px;color:var(--ink)}
.p3 .photo{left:49px;top:133px;width:334px;height:273px;border-radius:167px 167px 0 0;background:linear-gradient(180deg,#ecebe7 0%,#dddcd7 40%,#9fae97 62%,#4f6d48 78%,#3e5a38 100%)}
.p3 .headline{left:104px;top:331px;color:var(--white);font-size:22px}

/* post 4 */
.p4{background:var(--paper)}
.p4 .photo{left:60px;top:195px;width:250px;height:160px;border-radius:50%;background:radial-gradient(ellipse at center,#f1efeb 0%,#d9c3b3 60%,#e9e5df 100%)}
.p4 .headline{left:18px;top:16px;color:var(--ink);font-size:24px}
.p4 .site{left:66px;bottom:22px;color:var(--ink)}

/* post 5 */
.p5{background:var(--green)}
.p5 .photo{left:172px;top:0;width:236px;height:406px;background:linear-gradient(180deg,#e4e4e2 0%,#d4d3d0 40%,#a9775a 70%,#6e4a35 100%)}
.p5 .brand{left:20px;top:16px;color:var(--white)}
.p5 .headline{left:20px;top:172px;width:140px;color:var(--white);font-size:14px}
.p5 .site{left:20px;bottom:18px;color:var(--white)}

/* post 6 */
.p6{background:var(--mint-soft)}
.p6 .brand{left:24px;top:16px;color:var(--ink)}
.p6 .site{right:-10px;top:18px;color:var(--ink)}
.p6 .photo{left:96px;top:96px;width:208px;height:208px;border-radius:50%;background:linear-gradient(160deg,#3a4a5a 0%,#6a6f74 45%,#e6dcd2 80%,#f2ede6 100%)}
.p6 .headline{left:24px;top:338px;color:var(--ink);font-size:22px;white-space:nowrap}
</style>
</head>
<body>

<section class="post p1 row-1 col-1">
  <div class="photo" role="img" aria-label="Жилой дом у реки, катер на воде, зелёный тон"></div>
  <h2 class="headline">Комиссия риелтора —<br>это как скрытый налог</h2>
  <span class="site">navory.ru</span>
</section>

<section class="post p2 row-1 col-2">
  <div class="photo" role="img" aria-label="Мужчина в VR-очках и риелтор в офисе"></div>
  <div class="brand">navory<small>сервис продажи недвижимости</small></div>
  <h2 class="headline">Риелтор ≠ маг и волшебник</h2>
  <span class="site">navory.ru</span>
</section>

<section class="post p3 row-1 col-3">
  <svg class="deco" width="408" height="406" aria-hidden="true">
    <path d="M26 406 V300 A190 190 0 0 1 406 300 V406" fill="none" stroke="var(--green)" stroke-width="46"/>
  </svg>
  <div class="photo" role="img" aria-label="Высотный жилой дом среди деревьев"></div>
  <div class="brand">navory<small>сервис продажи недвижимости</small></div>
  <span class="site">navory.ru</span>
  <h2 class="headline">Кто работает —<br>вы или риелтор?</h2>
</section>

<section class="post p4 row-2 col-1">
  <svg class="deco" width="408" height="406" aria-hidden="true">
    <circle cx="200" cy="280" r="230" fill="var(--mint-soft)"/>
    <circle cx="200" cy="280" r="165" fill="var(--mint)"/>
  </svg>
  <div class="photo" role="img" aria-label="Ладонь с макетом жилого дома и деревьями"></div>
  <h2 class="headline">Риелтору выгодно,<br>чтобы вы продали дешевле</h2>
  <span class="site">navory.ru</span>
</section>

<section class="post p5 row-2 col-2">
  <svg class="deco" width="408" height="406" aria-hidden="true">
    <path d="M150 0 V406" stroke="var(--mint)" stroke-opacity=".45" stroke-width="1"/>
    <path d="M172 0 A90 90 0 0 0 82 90" fill="none" stroke="var(--mint)" stroke-opacity=".45"/>
  </svg>
  <div class="photo" role="img" aria-label="Бронзовая статуя Фемиды с весами"></div>
  <div class="brand">navory<small>сервис продажи недвижимости</small></div>
  <h2 class="headline">Юридические риски: риелтор не всегда спасает</h2>
  <span class="site">navory.ru</span>
</section>

<section class="post p6 row-2 col-3">
  <svg class="deco" width="408" height="406" aria-hidden="true">
    <path d="M40 406 V190 A160 160 0 0 1 360 190 V406" fill="none" stroke="var(--green)" stroke-opacity=".35"/>
    <path d="M70 406 V200 A130 130 0 0 1 330 200 V406" fill="none" stroke="var(--green)" stroke-opacity=".35"/>
  </svg>
  <div class="photo" role="img" aria-label="Девушка с телефоном и документами в кафе"></div>
  <div class="brand">navory<small>сервис продажи недвижимости</small></div>
  <span class="site">navory.ru</span>
  <h2 class="headline">Риелтор как такси за миллион</h2>
</section>

</body>
</html>
```